2.875 x 4 inch Ad for a Program Guide at Conference with 15,000

The ad needs to be 2.875 inches by 4 inches. I have attached some ideas. We definitely don't want a white background but we need the ad to visually jump off a page so our ad doesn't get lost. The mock-ups were something I put together so I could get a sense of what I wanted to say. I've also attached feedback from my business partners about these mock-ups.

Target Market(s)

Heads of Human Resources and Leadership Development, CEO's, COO's, and business owners.

Industry/Entity Type

Consulting

Font styles to use
Serif

Colors
6b449b
0355a3
0692cd
00a990
a64599
f37122

Requirements
Must have
• Colors from brand standards. Logo. Large lettering to be seen easily as a quarter page ad.
Nice to have
• Creativity... feeling of strength, warmth and business all at the same time.
Should not have
• Please note the updated logo. The name of the company is Vorrada Mindful Business.

```html
<!DOCTYPE html>
<html lang="en">
<head>
<meta charset="UTF-8">
<title>Vorrada Mindful Business – Program Guide Ad</title>
<link rel="stylesheet" href="https://fonts.googleapis.com/css2?family=Open+Sans:wght@300;400;700;800&display=swap">
<style>
  :root {
    --page: #e8e5e0;
    --mist-top: #cfe9e6;
    --mist-mid: #9fd6e2;
    --sky: #2fb0e3;
    --white: #ffffff;
    --orange: #f0913f;
    --purple: #5d2a78;
    --navy: #25417f;
    --brand-teal: #00a990;
  }
  html, body {
    margin: 0;
    width: 1200px;
    height: 815px;
    overflow: hidden;
    background: var(--page);
    font-family: "Open Sans", Arial, sans-serif;
  }
  .ad {
    position: absolute;
    left: 327px;
    top: 27px;
    width: 546px;
    height: 760px;
    overflow: hidden;
    background: linear-gradient(165deg, var(--mist-top) 0%, var(--mist-mid) 45%, var(--sky) 82%, var(--brand-teal) 100%);
    box-shadow: 0 6px 18px rgba(0,0,0,.18);
  }
  .ad__panel {
    position: absolute;
    inset: 0;
    width: 546px;
    height: 760px;
  }
  .brand {
    position: absolute;
    top: 28px;
    right: 26px;
    display: flex;
    align-items: center;
    gap: 10px;
  }
  .brand__dot {
    width: 34px;
    height: 34px;
    border-radius: 50%;
    background: var(--purple);
  }
  .brand__name {
    font-weight: 700;
    font-size: 17px;
    color: var(--navy);
    letter-spacing: .5px;
    line-height: 1.15;
  }
  .headline {
    position: absolute;
    left: 32px;
    top: 96px;
    margin: 0;
    color: var(--white);
    font-weight: 800;
    line-height: .9;
  }
  .headline__big { display: block; font-size: 92px; letter-spacing: -1px; }
  .headline__big--first { padding-left: 8px; }
  .headline__small { display: block; font-size: 60px; font-weight: 700; letter-spacing: 1px; margin-top: 4px; }
  .focus {
    position: absolute;
    left: 20px;
    top: 352px;
    margin: 0;
    color: var(--orange);
    font-weight: 700;
    font-size: 76px;
    line-height: .95;
  }
  .focus span { display: block; }
  .focus .focus__lead { padding-left: 22px; }
  .learn {
    position: absolute;
    left: 24px;
    top: 556px;
    margin: 0;
    color: var(--purple);
    font-weight: 300;
    font-size: 20px;
  }
  .formula {
    position: absolute;
    left: 190px;
    top: 552px;
    margin: 0;
    padding: 0;
    list-style: none;
    color: var(--purple);
    font-weight: 700;
    font-size: 21px;
    line-height: 1.3;
  }
  .formula__indent { padding-left: 17px; }
  .contact {
    position: absolute;
    left: 24px;
    bottom: 40px;
    margin: 0;
    color: var(--purple);
    font-weight: 400;
    font-size: 20px;
    line-height: 1.35;
  }
  .contact span { display: block; }
  .contact .contact__booth { padding-left: 40px; }
</style>
</head>
<body>
  <article class="ad">
    <svg class="ad__panel" viewBox="0 0 546 760" aria-hidden="true">
      <defs>
        <linearGradient id="panelFill" x1="0" y1="0" x2="0" y2="1">
          <stop offset="0" stop-color="#5677ab"/>
          <stop offset=".5" stop-color="#3f8fab"/>
          <stop offset="1" stop-color="#4bb79e"/>
        </linearGradient>
      </defs>
      <path fill="url(#panelFill)" d="M400 78 L546 70 L546 760 L175 760 L180 700 L170 640 L186 600 L182 540 L200 500 L196 440 L214 400 L212 350 L232 300 L240 250 L262 210 L300 170 L320 150 L350 128 L372 110 Z"/>
    </svg>

    <div class="brand">
      <span class="brand__dot"></span>
      <span class="brand__name">VORRADA<br>MINDFUL BUSINESS</span>
    </div>

    <h1 class="headline">
      <span class="headline__big headline__big--first">EXPLORE</span>
      <span class="headline__big">DEVELOP</span>
      <span class="headline__small">STRENGTHEN</span>
    </h1>

    <h2 class="focus">
      <span class="focus__lead">Leadership</span>
      <span>&amp; Culture</span>
    </h2>

    <p class="learn">Learn how:</p>

    <ul class="formula">
      <li>+ REAL Leadership</li>
      <li class="formula__indent">REAL Culture</li>
      <li>= REAL Results</li>
    </ul>

    <p class="contact">
      <span class="contact__booth">Booth 418</span>
      <span>www.vmbgroup.com</span>
    </p>
  </article>
</body>
</html>
```